Brochure Annual Report Design

I want to create a brochure / annual report for our company. Can you help me. I like this design. https://pixelstallhub.com/Brightfold/2847163-Annual-Report-2018. Here is our company website www.velmordental.com. Please take the logo from there. Our website needs an upgrade in how it looks. I would like the brochure annual report and the website to look somewhat congruent. I also want to create a very high end magazine that is fun for our company eventually.

We are a company that helps dentists create better practices by really improving the way they do business and motivating their teams. As a result they have more fun, more profit, happier team members, and they all have better lives.

Target Market(s)

dentist

Industry/Entity Type

Dental

Number of Pages Required

5+ page

Colors
0255a3
85cae6
ffffff

Requirements
Must have
• Must look really good.
Nice to have
• Any creative suggestions are welcomed. I need a website that looks congruent to the brochure and annual report. I also want to create a very high end magazine that is fun for our company eventually.
Should not have
• I don't like low quality design.

```html
<!DOCTYPE html>
<html lang="en">
<head>
<meta charset="utf-8">
<title>Annual Report – Message from our CEO &amp; The People</title>
<link href="https://fonts.googleapis.com/css2?family=Montserrat:wght@400;500;600;700;800;900&display=swap" rel="stylesheet">
<style>
  :root {
    --backdrop: #d6d7d9;
    --paper: #f4f5f6;
    --navy: #16294f;
    --brand-blue: #0255a3;
    --band-blue: #1b6fb3;
    --sky: #85cae6;
    --sky-deep: #62b5d6;
    --white: #ffffff;
    --photo-light: #c9c9c9;
    --photo-dark: #7c7c7c;
  }
  * { box-sizing: border-box; margin: 0; padding: 0; }
  html, body { width: 1200px; height: 833px; overflow: hidden; }
  body {
    background: var(--backdrop);
    font-family: "Montserrat", sans-serif;
    position: relative;
  }
  .spread {
    position: absolute;
    left: 140px; top: 92px;
    width: 920px; height: 650px;
    display: flex;
  }
  .page {
    position: relative;
    width: 460px; height: 650px;
    background: var(--paper);
    overflow: hidden;
  }
  .page--left { background: linear-gradient(to right, var(--paper) 88%, #e3e4e6 100%); }
  .page--right { background: linear-gradient(to left, var(--paper) 88%, #e3e4e6 100%); }
  .page-band {
    position: absolute; left: 0; right: 0; bottom: 0; height: 48px;
    background: linear-gradient(to right, var(--brand-blue), var(--band-blue));
  }
  .page--right .page-band { background: linear-gradient(to left, var(--brand-blue), var(--band-blue)); }

  /* CEO page */
  .ceo-block {
    position: absolute; left: 28px; top: 140px; width: 372px; bottom: 48px;
    background: linear-gradient(160deg, var(--sky-deep), var(--sky));
  }
  .ceo-title {
    position: absolute; left: 42px; top: 92px;
    font-weight: 900; font-size: 24px; line-height: 25px; letter-spacing: 0.5px;
    color: var(--navy); text-transform: uppercase;
  }
  .ceo-title .on-block { color: var(--white); }
  .ceo-portrait {
    position: absolute; left: 250px; top: 40px; width: 160px; height: 200px;
    border: 1px solid var(--brand-blue); padding: 6px; background: var(--paper);
  }
  .ceo-portrait .photo { width: 100%; height: 100%; }
  .ceo-caption {
    position: absolute; left: 214px; top: 250px;
    font-size: 9px; color: var(--navy);
  }
  .ceo-caption strong { display: block; font-weight: 600; font-size: 10px; }
  .ceo-letter {
    position: absolute; left: 62px; top: 284px; width: 320px;
    display: flex; gap: 22px;
    font-size: 9.5px; line-height: 14px; color: rgba(255,255,255,0.85);
  }
  .ceo-letter p { flex: 1; }

  /* Team page */
  .team-title {
    position: absolute; left: 40px; top: 48px; width: 380px;
    font-weight: 800; font-size: 21px; color: var(--navy); text-align: center;
  }
  .team-grid { position: absolute; left: 40px; top: 0; width: 380px; height: 600px; }
  .team-column { position: absolute; width: 120px; display: flex; flex-direction: column; gap: 8px; }
  .team-column:nth-child(1) { left: 0; top: 96px; }
  .team-column:nth-child(2) { left: 130px; top: 112px; }
  .team-column:nth-child(3) { left: 260px; top: 128px; }
  .member { position: relative; width: 120px; height: 104px; }
  .member .photo { position: absolute; left: 6px; top: 0; width: 108px; height: 92px; border: 1px solid var(--brand-blue); }
  .member-label {
    position: absolute; left: 0; right: 0; bottom: 0; min-height: 26px;
    background: var(--sky); padding: 3px 6px; color: var(--navy);
  }
  .member-name { font-size: 9px; font-weight: 600; line-height: 11px; white-space: nowrap; }
  .member-role { font-size: 6.5px; line-height: 8px; }

  .photo { background: radial-gradient(ellipse at 50% 45%, var(--photo-light), var(--photo-dark)); }
</style>
</head>
<body>
  <main class="spread">
    <section class="page page--left">
      <div class="ceo-block"></div>
      <h1 class="ceo-title">Message<br>From<br><span class="on-block">Our CEO</span></h1>
      <figure class="ceo-portrait">
        <div class="photo" role="img" aria-label="Black and white portrait photo of the founder and CEO"></div>
      </figure>
      <div class="ceo-caption"><strong>Warren Kessling</strong>Founder &amp; CEO</div>
      <div class="ceo-letter">
        <p>Every practice we coach begins with a clear plan and a team that believes in it. This year we grew together, listened closely and kept our promise to help dentists lead with purpose. We measured progress in calmer days, stronger schedules and happier patients across every region we serve.</p>
        <p>Our coaches brought fresh ideas, steady support and real results to each office. Looking ahead, we will keep investing in people, training and tools that make work more fun, more profitable and more meaningful for every doctor and team member we partner with.</p>
      </div>
      <div class="page-band"></div>
    </section>

    <section class="page page--right">
      <h2 class="team-title">Our Secret Sauce – The People</h2>
      <div class="team-grid">
        <div class="team-column">
          <div class="member"><div class="photo" role="img" aria-label="Portrait photo of Mara Lynn Holt"></div><div class="member-label"><div class="member-name">Mara Lynn Holt</div><div class="member-role">Director of Coaching</div></div></div>
          <div class="member"><div class="photo" role="img" aria-label="Portrait photo of Lori Vantassel"></div><div class="member-label"><div class="member-name">Lori Vantassel</div><div class="member-role">Lead Practice Coach</div></div></div>
          <div class="member"><div class="photo" role="img" aria-label="Portrait photo of Paula Brightwood"></div><div class="member-label"><div class="member-name">Paula Brightwood</div><div class="member-role">Lead Practice Coach</div></div></div>
          <div class="member"><div class="photo" role="img" aria-label="Portrait photo of Evan Rusk"></div><div class="member-label"><div class="member-name">Evan Rusk</div><div class="member-role">Business Development Analyst</div></div></div>
        </div>
        <div class="team-column">
          <div class="member"><div class="photo" role="img" aria-label="Portrait photo of Ruth Caldera"></div><div class="member-label"><div class="member-name">Ruth Caldera</div><div class="member-role">Chief Financial Officer</div></div></div>
          <div class="member"><div class="photo" role="img" aria-label="Portrait photo of Jenna Marlowe"></div><div class="member-label"><div class="member-name">Jenna Marlowe</div><div class="member-role">Lead Practice Coach</div></div></div>
          <div class="member"><div class="photo" role="img" aria-label="Portrait photo of Owen Carver"></div><div class="member-label"><div class="member-name">Owen Carver</div><div class="member-role">Executive Producer</div></div></div>
          <div class="member"><div class="photo" role="img" aria-label="Portrait photo of Colin Ashby"></div><div class="member-label"><div class="member-name">Colin Ashby</div><div class="member-role">Marketing &amp; Digital<br>Media Producer</div></div></div>
        </div>
        <div class="team-column">
          <div class="member"><div class="photo" role="img" aria-label="Portrait photo of Nadia Fernhill"></div><div class="member-label"><div class="member-name">Nadia Fernhill</div><div class="member-role">Lead Practice Coach &amp; Events</div></div></div>
          <div class="member"><div class="photo" role="img" aria-label="Portrait photo of Celia Drummond"></div><div class="member-label"><div class="member-name">Celia Drummond</div><div class="member-role">Lead Practice Coach</div></div></div>
          <div class="member"><div class="photo" role="img" aria-label="Portrait photo of Rachel Dunmore"></div><div class="member-label"><div class="member-name">Rachel Dunmore</div><div class="member-role">Business Development</div></div></div>
          <div class="member"><div class="photo" role="img" aria-label="Portrait photo of Dr. Graham Tolliver"></div><div class="member-label"><div class="member-name">Dr. Graham Tolliver</div><div class="member-role">Adjunct Faculty</div></div></div>
        </div>
      </div>
      <div class="page-band"></div>
    </section>
  </main>
</body>
</html>
```